DESSERT FLYER

We need a flyer design for desserts and drinks for our restaurant.

We use Retro/rustic as main theme

Flyer must include all images, which are attached to this project. We also named correctly for each images, so you can use for each dish's title (docx file)
Must include our logo as well.

Flyer tittle is "SWEET PLUMO"

Please see our website for reference at brickhollow.com.au

Flyer's printing size is A5 Vertical. Single Side

```html
<!DOCTYPE html>
<html lang="en">
<head>
<meta charset="utf-8">
<title>Sweet Plumo – Dessert Flyer</title>
<link rel="stylesheet" href="https://fonts.googleapis.com/css2?family=Chewy&family=Oswald:wght@400;500&display=swap">
<style>
  :root {
    --teal: #2f8f96;
    --teal-soft: #bfe4e2;
    --teal-pale: #e3f3f2;
    --orange: #f0893a;
    --ink: #2f2f2f;
    --paper: #fbfdfc;
    --rule: #f3a86b;
  }
  * { margin: 0; padding: 0; box-sizing: border-box; }
  html, body { width: 847px; height: 1200px; overflow: hidden; background: var(--paper); }
  .flyer {
    position: relative;
    width: 847px; height: 1200px; overflow: hidden;
    background: radial-gradient(ellipse 720px 900px at 230px 640px, var(--teal-soft) 0%, var(--teal-pale) 55%, var(--paper) 85%);
    font-family: "Oswald", sans-serif;
    color: var(--ink);
  }
  .title {
    position: absolute; left: 40px; top: 18px;
    font-family: "Chewy", cursive; font-weight: 400;
    color: var(--orange);
    font-size: 80px; line-height: 0.95; letter-spacing: 3px;
  }
  .title span { display: block; }
  .title span + span { margin-left: 60px; }
  .brand {
    position: absolute; right: 44px; top: 70px;
    font-weight: 500; color: var(--teal);
    font-size: 46px; letter-spacing: 3px; line-height: 1;
  }
  .dish { position: absolute; width: 320px; text-align: center; }
  .dish--left { left: 55px; }
  .dish--right { left: 477px; }
  .dish__photo {
    width: 230px; height: 230px; margin: 0 auto;
    border-radius: 50%; border: 5px solid #fff;
    box-shadow: 0 3px 10px rgba(0,0,0,.18);
  }
  .dish__name {
    margin-top: 10px;
    font-size: 19px; letter-spacing: 1px;
    text-transform: uppercase; line-height: 24px;
  }
  .dish__name small { font-size: 15px; line-height: 19px; display: block; }
  .dish__price { font-size: 18px; line-height: 22px; margin-top: 2px; }
  .photo--coconut { background: radial-gradient(circle at 50% 45%, #efe6d2, #b48a5c 60%, #6f8a52); }
  .photo--sticky { background: radial-gradient(circle at 40% 55%, #4b2d4a, #7b5a8a 40%, #f3c64d 70%, #e9e4d6); }
  .photo--fried { background: radial-gradient(circle at 50% 50%, #f6dcae, #d8914a 45%, #5a7a4c 80%); }
  .photo--fritter { background: radial-gradient(circle at 50% 50%, #e0a23c, #b86b22 45%, #3f6a33 80%); }
  .photo--sago { background: radial-gradient(circle at 50% 50%, #f4f4ef, #cfd6c8 45%, #3f7a3a 80%); }
  .photo--coffee { background: radial-gradient(circle at 50% 45%, #a78056, #5a3a24 55%, #2a1a12); }
  .divider { position: absolute; left: 378px; width: 100px; height: 2px; background: var(--rule); }
</style>
</head>
<body>
<main class="flyer">
  <h1 class="title"><span>SWEET</span><span>PLUMO</span></h1>
  <div class="brand">BRICK HOLLOW</div>

  <div class="divider" style="top:500px;"></div>
  <div class="divider" style="top:822px;"></div>
  <div class="divider" style="top:1140px;"></div>

  <section class="dish dish--left" style="top:225px;">
    <div class="dish__photo photo--coconut" role="img" aria-label="Photo of a fresh young coconut with a straw"></div>
    <p class="dish__name">Fresh Young Coconut Juice</p>
    <p class="dish__price">$5.50</p>
  </section>

  <section class="dish dish--right" style="top:180px;">
    <div class="dish__photo photo--fritter" role="img" aria-label="Photo of banana fritters with vanilla ice-cream on a banana leaf"></div>
    <p class="dish__name">Banana Fritter with<br>Vanilla Ice-Cream</p>
    <p class="dish__price">$6.90</p>
  </section>

  <section class="dish dish--left" style="top:545px;">
    <div class="dish__photo photo--sticky" role="img" aria-label="Photo of black sticky rice with mango slices"></div>
    <p class="dish__name">Black Sticky Rice with Mango</p>
    <p class="dish__price">$6.90</p>
  </section>

  <section class="dish dish--right" style="top:522px;">
    <div class="dish__photo photo--sago" role="img" aria-label="Photo of banana sago pudding on a leaf"></div>
    <p class="dish__name">Banana Sago Pudding with<br>Peanut Topping</p>
    <p class="dish__price">$6.90</p>
  </section>

  <section class="dish dish--left" style="top:862px;">
    <div class="dish__photo photo--fried" role="img" aria-label="Photo of fried ice-cream with caramel topping"></div>
    <p class="dish__name">Fried Ice-Cream with<small>Caramel/Chocolate/<br>Strawberry Topping</small></p>
    <p class="dish__price">$6.90</p>
  </section>

  <section class="dish dish--right" style="top:870px;">
    <div class="dish__photo photo--coffee" role="img" aria-label="Photo of Vietnamese drip coffee with coffee beans"></div>
    <p class="dish__name">Vietnamese Coffee</p>
    <p class="dish__price">$6.90</p>
  </section>
</main>
</body>
</html>
```